Navigate the Underground Car Park to 7K3R Vet Clinic

Eye-catching signage for Underground Carpark.
We want to help new Clients, or those with bad senses of direction, to the correct Lift Lobby.
We want to be able to say 'Just follow the signs'.

It can be confusing and many other business have utilised some of the pillars in the carpark to guide their customers to the right place.

People don't want to walk far with sick animals so it is important they get to the right Lift Lobby.
Updates

We are thinking instead of 'Just Follow the Signs,We would like to try:'Looking for us?' (Large Text)'Follow the Signs (much smaller Text)Also, it is very useful to see the proposed sign dropped on to the photo of the car park pillars I included.Many thanks Added Friday, June 16, 2017

Target Market(s)

Customers, coming for the 1st time, trying to navigate the Underground CarPark towards the appropriate Lift lobby

Industry/Entity Type

Veterinary

Font styles to use
Serif

Colors
f78f20
00a990
0455a3

Requirements
Must have
• Logo.
• Bright. Clear. Not too cluttered.
• Warmth. Humour. Approachable.
• Please include: Building 4, Mezzanine Level
Nice to have
• Please look at our FB pages and Instagram page @7k3rvetclinic for a good feel of who we are.
• Some level of style or image continuity with the Pet Tips Poster (see attached file)
Should not have
• Not have a medical feel

```html
<!DOCTYPE html>
<html lang="en">
<head>
<meta charset="utf-8">
<title>7K3R Vet Clinic – Looking For Us? Car Park Sign</title>
<link rel="stylesheet" href="https://fonts.googleapis.com/css2?family=Montserrat:wght@400;600;700;800&display=swap">
<style>
  :root {
    --page-bg: #f2f2f2;
    --poster-bg: #ffffff;
    --sage: #93c2ad;
    --sage-soft: #a8cfbd;
    --teal-ink: #2e6b7a;
    --orange: #e08a2c;
    --orange-soft: #e9a35a;
    --pattern-tint: #f7f2ec;
    --white: #ffffff;
    --photo-tan: #c69a6a;
    --photo-shadow: #8a6544;
    --scene-blue: #5f7e96;
    --scene-dark: #2f3e4c;
  }
  * { box-sizing: border-box; margin: 0; padding: 0; }
  html, body {
    width: 1026px; height: 1200px; overflow: hidden;
    background: var(--page-bg);
    font-family: "Montserrat", sans-serif;
  }
  .poster {
    position: absolute; left: 113px; top: 20px;
    width: 800px; height: 1160px;
    background: var(--poster-bg);
    border: 9px solid var(--sage);
  }
  .brand {
    position: absolute; left: 0; right: 0; top: 150px;
    display: flex; flex-direction: column; align-items: center;
  }
  .brand-row { display: flex; align-items: center; gap: 14px; }
  .brand-dot {
    width: 34px; height: 34px; border-radius: 50%;
    background: var(--orange);
  }
  .brand-name {
    font-size: 40px; font-weight: 600; color: var(--teal-ink);
    letter-spacing: 0.5px;
  }
  .brand-tagline {
    margin-top: 6px;
    font-size: 11px; font-weight: 400; letter-spacing: 4px;
    color: var(--teal-ink);
  }
  .headline-box {
    position: absolute; left: 28px; top: 250px;
    width: 738px; height: 154px;
    border: 2px solid var(--orange); border-radius: 22px;
    text-align: center; padding-top: 16px;
  }
  .headline {
    font-size: 59px; font-weight: 800; color: var(--teal-ink);
    letter-spacing: 1px; line-height: 1.15;
  }
  .subline {
    font-size: 33px; font-weight: 700; color: var(--orange);
    margin-top: 6px;
  }
  .pattern-band {
    position: absolute; left: 0; right: 0; top: 420px; height: 455px;
    background: linear-gradient(180deg, var(--pattern-tint), #fbf8f4 60%, var(--pattern-tint));
  }
  .dog-photo {
    position: absolute; left: 374px; top: 560px;
    width: 380px; height: 370px;
    border-radius: 48% 48% 10px 10px;
    background: radial-gradient(ellipse at 55% 40%, var(--photo-tan), var(--photo-shadow) 80%);
  }
  .find-badge { position: absolute; left: 30px; top: 449px; width: 320px; height: 320px; }
  .open-badge {
    position: absolute; left: 297px; top: 745px;
    width: 140px; height: 140px; border-radius: 50%;
    background: var(--sage-soft);
    display: flex; flex-direction: column; justify-content: center; align-items: center;
    color: var(--white); font-size: 27px; font-weight: 400; line-height: 1.3;
  }
  .info-strip {
    position: absolute; left: 39px; top: 927px;
    width: 727px; height: 160px;
    display: flex; border-radius: 16px; overflow: hidden;
  }
  .team-scene {
    flex: 0 0 463px;
    background: linear-gradient(180deg, var(--scene-blue), var(--scene-dark));
  }
  .contact-card {
    flex: 1; background: var(--orange); color: var(--white);
    padding: 12px 14px; border-radius: 16px 0 0 16px; margin-left: -14px;
  }
  .contact-title { font-size: 20px; font-weight: 700; margin-bottom: 8px; }
  .contact-lines { font-size: 12.5px; font-weight: 700; line-height: 1.55; }
  .contact-body { font-size: 12px; font-weight: 400; line-height: 1.4; margin-top: 6px; opacity: .95; }
  .footer-brand {
    position: absolute; left: 0; right: 0; top: 1105px;
    display: flex; justify-content: center; align-items: center; gap: 6px;
  }
  .footer-dot { width: 12px; height: 12px; border-radius: 50%; background: var(--orange); }
  .footer-name { font-size: 14px; font-weight: 600; color: var(--teal-ink); }
</style>
</head>
<body>
  <main class="poster">
    <header class="brand">
      <div class="brand-row">
        <span class="brand-dot"></span>
        <span class="brand-name">7K3R Vet Clinic</span>
      </div>
      <span class="brand-tagline">VETERINARY CLINIC</span>
    </header>

    <section class="headline-box">
      <h1 class="headline">LOOKING FOR US?</h1>
      <p class="subline">Keep Calm and Follow the Signs</p>
    </section>

    <div class="pattern-band" role="img" aria-label="Faint repeating pattern of little dog figures in orange and sage"></div>

    <div class="dog-photo" role="img" aria-label="Photograph of a happy tan dog with floppy ears, smiling at the viewer"></div>

    <svg class="find-badge" viewBox="0 0 320 320" aria-labelledby="find-title">
      <title id="find-title">Where to find us: Silver Bay Arcade, Building 4, Mezzanine Level, above Cafe Lumen</title>
      <defs>
        <path id="ring-path" d="M39.7 203.8 A128 128 0 1 1 280.3 203.8"/>
      </defs>
      <circle cx="160" cy="160" r="152" fill="var(--white)" stroke="var(--sage)" stroke-width="8"/>
      <circle cx="160" cy="160" r="110" fill="none" stroke="var(--sage)" stroke-width="3" stroke-dasharray="14 7"/>
      <circle cx="160" cy="160" r="100" fill="var(--orange)"/>
      <text font-family="Montserrat, sans-serif" font-size="29" font-weight="700" fill="var(--teal-ink)" letter-spacing="7">
        <textPath href="#ring-path" startOffset="50%" text-anchor="middle">WHERE TO FIND US?</textPath>
      </text>
      <g font-family="Montserrat, sans-serif" fill="var(--white)" text-anchor="middle" font-weight="700">
        <text x="160" y="138" font-size="18">Silver Bay Arcade</text>
        <text x="160" y="162" font-size="18">Building 4,</text>
        <text x="160" y="186" font-size="18">Mezzanine Level</text>
        <text x="160" y="207" font-size="13" font-weight="600">(Above Cafe Lumen)</text>
      </g>
    </svg>

    <div class="open-badge"><span>Open</span><span>7/7</span></div>

    <section class="info-strip">
      <div class="team-scene" role="img" aria-label="Playful photo of toy vet figures with small pets in a clinic room"></div>
      <div class="contact-card">
        <h2 class="contact-title">Contact Info</h2>
        <p class="contact-lines">The Crescent: + 800 7K3RVet |<br>Cedar Heights: 971 4 555 0187</p>
        <p class="contact-body">Lorem ipsum dolor sit amet, consectetur adipisicing elit, sdo eiusmod tempor incididunt ut</p>
      </div>
    </section>

    <footer class="footer-brand">
      <span class="footer-dot"></span>
      <span class="footer-name">7K3R Vet Clinic</span>
    </footer>
  </main>
</body>
</html>
```